Design My Bussiness Card
Technology company
Project: Design My Bussiness Card
Design My Bussiness Card -
Creative Brief
Professional
Dorian Pelkey
2847 E. Tollbrook #3
marisa@vantrelo.net
www.qoribelix.info

```html
<!DOCTYPE html>
<html lang="en">
<head>
<meta charset="utf-8">
<title>Qoribelix Business Card</title>
<link rel="stylesheet" href="https://fonts.googleapis.com/css2?family=Goudy+Bookletter+1911&display=swap">
<style>
  :root {
    --page: #ffffff;
    --card: #ffffff;
    --green-dark: #2f8a1f;
    --green: #4aa82c;
    --green-light: #8fcf4a;
    --brown: #6b3a1c;
    --ink: #2a2a2a;
    --label: #9a2a1a;
    --shadow: rgba(0, 0, 0, 0.28);
  }
  * { margin: 0; padding: 0; box-sizing: border-box; }
  html, body {
    width: 1200px; height: 799px; overflow: hidden;
    background: var(--page);
    font-family: "Goudy Bookletter 1911", Georgia, serif;
  }
  .canvas { position: relative; width: 1200px; height: 799px; }
  .card {
    position: absolute; left: 283px; width: 581px; height: 355px;
    background: var(--card); overflow: hidden;
    box-shadow: 0 3px 10px var(--shadow);
  }
  .card--front { top: 36px; }
  .card--back { top: 415px; }
  .card__art { position: absolute; inset: 0; width: 100%; height: 100%; }

  .brand {
    position: absolute; left: 30px; top: 22px;
    display: flex; align-items: center; gap: 10px;
  }
  .brand__mark {
    width: 34px; height: 34px; border-radius: 50%;
    background: var(--green);
  }
  .brand__name {
    font-size: 32px; color: var(--green-dark); letter-spacing: 0.5px;
  }

  .person { position: absolute; left: 30px; top: 98px; color: var(--ink); }
  .person__name { font-size: 40px; line-height: 1; color: #1f1f1f; margin-bottom: 16px; }
  .person__line { font-size: 17px; line-height: 27px; }
  .person__line--small { font-size: 14px; line-height: 22px; }
  .person__label { color: var(--label); }

  .web {
    position: absolute; color: #ffffff; font-size: 25px; letter-spacing: 2.5px;
  }
  .card--front .web { left: 30px; top: 302px; }
  .card--back .web { left: 0; right: 0; top: 22px; text-align: center; }
</style>
</head>
<body>
<div class="canvas">

  <section class="card card--front">
    <svg class="card__art" viewBox="0 0 581 355" aria-hidden="true">
      <defs>
        <linearGradient id="bandFront" x1="0" y1="0" x2="0" y2="1">
          <stop offset="0" stop-color="#a6d95a"/>
          <stop offset="0.45" stop-color="#4aa82c"/>
          <stop offset="1" stop-color="#2f8a1f"/>
        </linearGradient>
        <radialGradient id="markFront" cx="0.4" cy="0.35" r="0.7">
          <stop offset="0" stop-color="#9ad84e"/>
          <stop offset="1" stop-color="#2f8a1f"/>
        </radialGradient>
      </defs>
      <path d="M0 250 C150 272 360 262 581 205 L581 355 L0 355 Z" fill="var(--brown)"/>
      <path d="M0 262 C150 282 360 272 581 214 L581 355 L0 355 Z" fill="url(#bandFront)"/>
      <circle cx="515" cy="250" r="62" fill="url(#markFront)"/>
    </svg>

    <div class="brand">
      <span class="brand__mark"></span>
      <span class="brand__name">Qoribelix</span>
    </div>

    <div class="person">
      <h1 class="person__name">Dorian Pelkey</h1>
      <p class="person__line">2847 E. Tollbrook #3</p>
      <p class="person__line person__line--small"><span class="person__label">Phone:</span> 5550142837&nbsp;&nbsp;<span class="person__label">Cell:</span> 5550142837</p>
      <p class="person__line person__line--small"><span class="person__label">Email:</span> marisa@vantrelo.net</p>
    </div>

    <p class="web">www.qoribelix.info</p>
  </section>

  <section class="card card--back">
    <svg class="card__art" viewBox="0 0 581 355" aria-hidden="true">
      <defs>
        <linearGradient id="bandBack" x1="0" y1="0" x2="0" y2="1">
          <stop offset="0" stop-color="#2f8a1f"/>
          <stop offset="0.6" stop-color="#4aa82c"/>
          <stop offset="1" stop-color="#a6d95a"/>
        </linearGradient>
        <radialGradient id="markBack" cx="0.4" cy="0.35" r="0.7">
          <stop offset="0" stop-color="#9ad84e"/>
          <stop offset="1" stop-color="#2f8a1f"/>
        </radialGradient>
      </defs>
      <path d="M0 0 L581 0 L581 112 C420 82 200 72 0 88 Z" fill="var(--brown)"/>
      <path d="M0 0 L581 0 L581 100 C420 70 200 60 0 76 Z" fill="url(#bandBack)"/>
      <circle cx="290" cy="232" r="56" fill="url(#markBack)"/>
    </svg>
    <p class="web">www.qoribelix.info</p>
  </section>

</div>
</body>
</html>
```